We need a web page design for a new company called "Quarry". We provide an innovative music sharing mobile application that allows music listeners to share their music without paying for a monthly subscription. We would like to incorporate the attached logo and color scheme. The final design should communicate music gifting and sharing.

Industry/Entity Type

It Company

```html
<!DOCTYPE html>
<html lang="en">
<head>
<meta charset="utf-8">
<title>Quarry — Discover</title>
<link href="https://fonts.googleapis.com/css2?family=Roboto:wght@300;400;500;700&display=swap" rel="stylesheet">
<style>
:root{
  --green:#5ea313;
  --green-soft:#dff3c8;
  --side:#222c35;
  --side-deep:#1b242c;
  --side-text:#c3c8cd;
  --side-muted:#7d868e;
  --player:#4a5766;
  --page:#f1f3f6;
  --white:#ffffff;
  --ink:#4a4f55;
  --ink-soft:#8a9097;
  --heading:#9ba3ab;
  --line:#e6e9ec;
  --red:#e94b4b;
  --amber:#f3b51b;
  --online:#5cb82a;
  --teal:#43b4c9;
  --indigo:#5b6bbf;
}
*{box-sizing:border-box;margin:0;padding:0}
html,body{width:1200px;height:876px;overflow:hidden}
body{position:relative;font-family:'Roboto',sans-serif;background:var(--page);color:var(--ink)}

/* brand + sidebar */
.brand{position:absolute;left:0;top:0;width:186px;height:56px;background:var(--green);display:flex;align-items:center;padding-left:30px;gap:8px}
.brand-dot{width:20px;height:20px;border-radius:50%;background:var(--white)}
.brand-name{color:var(--white);font-size:24px;font-weight:500}
.sidebar{position:absolute;left:0;top:56px;width:186px;height:763px;background:var(--side)}
.nav-title{color:var(--green);font-size:14px;font-weight:500;padding:13px 0 0 19px;height:38px}
.nav-item{display:flex;align-items:center;height:35px;padding:0 18px;color:var(--side-text);font-size:13px}
.nav-item svg{width:14px;height:14px;margin-right:15px;flex:none}
.nav-item .label{flex:1}
.nav-item.sub svg{stroke:var(--side-muted)}
.nav-section{display:flex;justify-content:space-between;align-items:center;color:var(--side-muted);font-size:11px;padding:0 13px;height:38px;margin-top:18px}
.nav-section + .nav-item{margin-top:-3px}
.count{min-width:14px;height:14px;border-radius:7px;font-size:9px;color:var(--white);display:flex;align-items:center;justify-content:center;padding:0 3px}
.count.indigo{background:var(--indigo)}
.count.green{background:var(--online)}
.chev{color:var(--side-muted);font-size:12px}

/* top bar */
.topbar{position:absolute;left:186px;top:0;width:1014px;height:56px;background:var(--white);display:flex;align-items:center}
.topbar .menu{margin-left:19px}
.topbar .search{display:flex;align-items:center;margin-left:36px;color:var(--ink-soft);font-size:12px;gap:14px}
.topbar .bell{position:absolute;left:820px;top:18px}
.bell-badge{position:absolute;left:7px;top:-7px;width:14px;height:14px;border-radius:50%;background:var(--red);color:var(--white);font-size:9px;display:flex;align-items:center;justify-content:center}
.topbar .user{position:absolute;left:880px;top:19px;font-size:13px;color:var(--ink)}
.topbar .avatar{position:absolute;left:968px;top:10px;width:34px;height:34px;border-radius:50%;background:radial-gradient(circle at 50% 40%,#6b5548,#2a2522 70%,#eee 71%)}

/* main */
.main{position:absolute;left:186px;top:56px;width:788px;height:763px;overflow:hidden}
.scroll-track{position:absolute;right:2px;top:8px;width:5px;height:540px;background:#c9cdd1;border-radius:3px}
.section-title{position:absolute;font-size:21px;font-weight:300;color:var(--heading)}
.refresh{position:absolute;left:733px;top:27px}
.eq{position:absolute;left:140px;top:28px}
.cover-grid{position:absolute;left:29px;top:64px;display:grid;grid-template-columns:repeat(6,105px);column-gap:18.3px;row-gap:0}
.card{height:218px}
.cover{position:relative;width:105px;height:157px;border-radius:2px;overflow:hidden}
.card-title{margin-top:14px;font-size:12.5px;color:var(--ink);white-space:nowrap;overflow:hidden;text-overflow:ellipsis}
.card-sub{margin-top:3px;font-size:10.5px;color:var(--ink-soft)}
.time-pill{position:absolute;left:9px;bottom:10px;background:var(--teal);color:var(--white);font-size:10px;font-weight:500;border-radius:9px;padding:2px 7px}
.num-pill{position:absolute;right:9px;top:9px;border-radius:9px;font-size:10px;padding:2px 6px}
.num-pill.teal{background:var(--teal);color:var(--white)}
.num-pill.light{background:var(--white);color:var(--ink)}
.stars{position:absolute;left:13px;top:8px;font-size:12px;letter-spacing:1px;color:#7fd1e0}
.stars .off{color:rgba(255,255,255,.55)}
.overlay-icon{position:absolute}
.bookmark{position:absolute;right:12px;top:0}

.song-grid{position:absolute;left:31px;top:541px;display:grid;grid-template-columns:repeat(4,88px);column-gap:18.6px}
.song{height:148px}
.song-art{width:88px;height:88px}
.song-title{margin-top:15px;font-size:12.5px;color:var(--ink)}
.song-sub{margin-top:3px;font-size:10.5px;color:var(--ink-soft)}

.top-list{position:absolute;left:469px;top:541px;width:282px;background:var(--white)}
.top-row{display:flex;align-items:center;height:67px;border-bottom:1px solid var(--line);padding:0 14px}
.top-row .thumb{width:38px;height:38px;border-radius:50%;flex:none;margin-right:14px}
.top-row .meta{flex:1}
.top-row .t{font-size:12.5px;color:var(--ink)}
.top-row .b{font-size:11.5px;color:var(--ink-soft);margin-top:4px}
.top-row .rank{font-size:24px;font-weight:300;color:#9aa0a6}

/* connected */
.connected{position:absolute;left:974px;top:56px;width:226px;height:763px;background:var(--green-soft)}
.connected h2{font-size:21px;font-weight:300;color:#93a38c;padding:23px 0 0 20px;height:62px}
.member{position:absolute;left:19px;display:flex;align-items:center}
.member .pic{position:relative;width:48px;height:48px;border-radius:50%;margin-right:10px}
.member .dot{position:absolute;right:0;top:1px;width:11px;height:11px;border-radius:50%;border:2px solid var(--green-soft)}
.dot.on{background:var(--online)}.dot.busy{background:var(--red)}.dot.away{background:var(--amber)}
.member .name{font-size:15px;color:var(--ink)}
.member .place{font-size:11px;color:var(--ink-soft);margin-top:3px}

/* bottom bar */
.me{position:absolute;left:0;top:819px;width:186px;height:57px;background:var(--side-deep);display:flex;align-items:center;padding-left:13px}
.me .pic{position:relative;width:38px;height:38px;border-radius:50%;background:radial-gradient(circle at 50% 45%,#8a8a8a,#3d3d3d 70%,#ddd 71%);margin-right:14px}
.me .pic i{position:absolute;left:0;top:0;width:9px;height:9px;border-radius:50%;background:var(--online)}
.me .n{color:var(--white);font-size:13px;font-weight:700}
.me .r{color:var(--side-muted);font-size:11px;margin-top:2px}
.player{position:absolute;left:186px;top:819px;width:788px;height:57px;background:var(--player);display:flex;align-items:center}
.controls{display:flex;align-items:center;gap:16px;padding-left:24px;width:179px}
.now-playing{width:224px;height:57px;background:var(--green);color:var(--white);font-size:13px;font-weight:500;display:flex;align-items:center;justify-content:center}
.timeline{display:flex;align-items:center;color:#d9dde1;font-size:11px;padding-left:34px;gap:14px}
.volume{width:48px;height:4px;border-radius:2px;background:#7d8894;position:relative}
.volume::before{content:"";position:absolute;left:0;top:0;width:36px;height:4px;border-radius:2px;background:#d9dde1}
.member-search{position:absolute;left:974px;top:819px;width:226px;height:57px;background:var(--side);display:flex;align-items:center;padding-left:23px;gap:12px}
.member-search .field{width:170px;border-bottom:1px solid #6b757e;color:#c3c8cd;font-size:11px;padding:0 0 6px 10px;margin-top:6px}
</style>
</head>
<body>

<div class="brand"><span class="brand-dot"></span><span class="brand-name">Quarry</span></div>

<nav class="sidebar">
  <div class="nav-title">Discover</div>
  <div class="nav-item"><svg viewBox="0 0 14 14" fill="none" stroke="#3fae6a" stroke-width="1.4"><circle cx="7" cy="7" r="5.5"/><path d="M4 5c2-1 4-1 6 1M4.5 8c2-1 3.5-.5 5 .5"/></svg><span class="label">What's New</span></div>
  <div class="nav-item"><svg viewBox="0 0 14 14" fill="none" stroke="#3fae6a" stroke-width="1.4"><path d="M5 11V3l7-1.5V9"/><circle cx="3.5" cy="11" r="1.5"/><circle cx="10.5" cy="9.5" r="1.5"/></svg><span class="label">Genres</span></div>
  <div class="nav-item"><svg viewBox="0 0 14 14" fill="none" stroke="#3fae6a" stroke-width="1.4"><rect x="1.5" y="3" width="11" height="8" rx="1"/><path d="M1.5 4l5.5 4 5.5-4"/></svg><span class="label">Share</span><span class="count indigo">6</span></div>
  <div class="nav-item"><svg viewBox="0 0 14 14" fill="none" stroke="#3fae6a" stroke-width="1.4"><path d="M4 3.5h9M4 7h9M4 10.5h9M1 3.5h1M1 7h1M1 10.5h1"/></svg><span class="label">Listen</span></div>
  <div class="nav-item"><svg viewBox="0 0 14 14" fill="none" stroke="#3fae6a" stroke-width="1.4"><rect x="1" y="3" width="12" height="8" rx="1.5"/><path d="M6 5.5v3l2.5-1.5z"/></svg><span class="label">Video</span></div>

  <div class="nav-section">Interface</div>
  <div class="nav-item sub"><svg viewBox="0 0 14 14" fill="none" stroke-width="1.3"><rect x="1" y="2" width="12" height="8" rx="1"/><path d="M5 12.5h4"/></svg><span class="label">Layouts</span><span class="chev">‹</span></div>
  <div class="nav-item sub"><svg viewBox="0 0 14 14" fill="none" stroke-width="1.3"><path d="M6 1.5h2M7 1.5v7M4.5 12.5l2.5-4 2.5 4"/></svg><span class="label">UI Kit</span><span class="chev">‹</span></div>
  <div class="nav-item sub"><svg viewBox="0 0 14 14" fill="none" stroke-width="1.3"><rect x="1" y="1" width="5" height="5"/><rect x="8" y="1" width="5" height="5"/><rect x="1" y="8" width="5" height="5"/><rect x="8" y="8" width="5" height="5"/></svg><span class="label">Pages</span><span class="chev">‹</span></div>

  <div class="nav-section">Playlist <svg width="16" height="16" viewBox="0 0 16 16" fill="none" stroke="#c3c8cd" stroke-width="1.2"><circle cx="8" cy="8" r="7"/><path d="M8 4.5v7M4.5 8h7"/></svg></div>
  <div class="nav-item sub"><svg viewBox="0 0 14 14" fill="none" stroke-width="1.3"><path d="M7 11V2l3 1.5"/><circle cx="5.5" cy="11" r="1.5"/></svg><span class="label">Hip-Pop</span></div>
  <div class="nav-item"><svg viewBox="0 0 14 14" fill="none" stroke="#3fae6a" stroke-width="1.3"><path d="M5 11V2l4 1.5M8 6h5M8 9h5"/><circle cx="3.5" cy="11" r="1.5"/></svg><span class="label">Jazz</span><span class="count green">9</span></div>
</nav>

<header class="topbar">
  <svg class="menu" width="14" height="12" viewBox="0 0 14 12" fill="none" stroke="#6b7279" stroke-width="1.4"><path d="M0 1h14M4 4.5h10M4 8h10M0 11h14"/></svg>
  <div class="search"><svg width="12" height="12" viewBox="0 0 12 12" fill="none" stroke="#6b7279" stroke-width="1.5"><circle cx="5" cy="5" r="4"/><path d="M8 8l3.5 3.5"/></svg>Search songs, albums...</div>
  <div class="bell"><svg width="14" height="16" viewBox="0 0 14 16" fill="none" stroke="#8a9097" stroke-width="1.3"><path d="M2 12V7a5 5 0 0 1 10 0v5l1 1H1z M5.5 14.5h3"/></svg><span class="bell-badge">3</span></div>
  <div class="user">John.Smith ▾</div>
  <div class="avatar" role="img" aria-label="Profile photo of John Smith"></div>
</header>

<main class="main">
  <div class="scroll-track"></div>
  <h2 class="section-title" style="left:26px;top:23px">Discover</h2>
  <svg class="eq" width="19" height="16" viewBox="0 0 19 16"><rect x="0" y="6" width="3" height="10" fill="#43b4c9"/><rect x="4" y="2" width="3" height="14" fill="#5b6bbf"/><rect x="8" y="4" width="3" height="12" fill="#5ea313"/><rect x="12" y="8" width="3" height="8" fill="#f3b51b"/><rect x="16" y="5" width="3" height="11" fill="#e94b4b"/></svg>
  <svg class="refresh" width="18" height="18" viewBox="0 0 18 18" fill="none" stroke="#9aa0a6" stroke-width="1.6"><path d="M3 9a6 6 0 0 1 10-4.5M15 9a6 6 0 0 1-10 4.5M13 1.5v3h-3M5 16.5v-3h3"/></svg>

  <section class="cover-grid">
    <article class="card"><div class="cover" role="img" aria-label="Album cover: girl in white dress standing on grass" style="background:linear-gradient(180deg,#4f5a38,#7c7a58 45%,#4a4a2a)"><span class="time-pill">03:20</span></div><div class="card-title">Tempered Song</div><div class="card-sub">Miaow</div></article>
    <article class="card"><div class="cover" style="background:linear-gradient(180deg,#3b3d40,#2a2c2f)" role="img" aria-label="Album cover in dark grey tones"><span class="stars">★★★<span class="off">☆☆</span></span>
      <svg class="overlay-icon" style="left:40px;top:63px" width="26" height="30" viewBox="0 0 26 30" fill="none" stroke="#fff" stroke-width="1.6"><path d="M2 2l22 13L2 28z"/></svg>
      <svg class="overlay-icon" style="left:14px;top:132px" width="11" height="11" viewBox="0 0 11 11"><circle cx="5.5" cy="5.5" r="5.5" fill="#fff"/><path d="M5.5 3v5M3 5.5h5" stroke="#2a2c2f" stroke-width="1.4"/></svg>
      <svg class="overlay-icon" style="left:77px;top:131px" width="14" height="12" viewBox="0 0 14 12"><path d="M7 12L1 6a3.3 3.3 0 0 1 6-4 3.3 3.3 0 0 1 6 4z" fill="#e94b4b"/></svg></div><div class="card-title">Vivamus vel tincidunt</div><div class="card-sub">Lauren Taylor</div></article>
    <article class="card"><div class="cover" role="img" aria-label="Album cover: railway track in misty forest" style="background:linear-gradient(180deg,#b9c2b6,#8f9a8c 55%,#59604f)"></div><div class="card-title">Morbi id neque quam</div><div class="card-sub">Allen JH</div></article>
    <article class="card"><div class="cover" role="img" aria-label="Album cover: figure standing by a lake" style="background:linear-gradient(180deg,#a6b8c8,#c9d1d6 50%,#6d7c84 70%,#3a3d3a)"><svg class="bookmark" width="12" height="14" viewBox="0 0 12 14"><path d="M0 0h12v14L6 10 0 14z" fill="#fff"/></svg></div><div class="card-title">Tincidunt libero</div><div class="card-sub">Amanda Conlan</div></article>
    <article class="card"><div class="cover" role="img" aria-label="Album cover: golden hills at sunset" style="background:linear-gradient(180deg,#c9b68e,#9a8460 45%,#5b4a32)"></div><div class="card-title">Fermentum diam</div><div class="card-sub">Nisa Colen</div></article>
    <article class="card"><div class="cover" role="img" aria-label="Album cover: snowy mountain peak" style="background:linear-gradient(180deg,#8fa7b8,#c7d0d6 45%,#5d6e7a 75%,#3f4a52)"><span class="num-pill teal">6</span></div><div class="card-title">Habitant</div><div class="card-sub">Dan Doorack</div></article>

    <article class="card"><div class="cover" role="img" aria-label="Album cover: couple sitting on a bench" style="background:linear-gradient(180deg,#d9b98a,#b8864e 60%,#8a5a2c)"><span class="num-pill light">12</span></div><div class="card-title">Vivamus vel tincidunt</div><div class="card-sub">Ligula H</div></article>
    <article class="card"><div class="cover" role="img" aria-label="Album cover: old railway track" style="background:linear-gradient(180deg,#d7d6b8,#9c9a72 50%,#4f4b34)"></div><div class="card-title">Aliquam sollicitudin</div><div class="card-sub">James East</div></article>
    <article class="card"><div class="cover" role="img" aria-label="Album cover: woman with sunglasses and flowers" style="background:linear-gradient(180deg,#f2dca6,#d9b77a 50%,#8f7c58)"></div><div class="card-title">Lementum ligula vitae</div><div class="card-sub">Lauren Taylor</div></article>
    <article class="card"><div class="cover" style="background:#c7dbe2" role="img" aria-label="Album cover in pale blue"><span class="stars" style="color:#43b4c9">★★★★<span class="off" style="color:#fff">☆</span></span>
      <svg class="overlay-icon" style="left:42px;top:64px" width="20" height="28" viewBox="0 0 20 28" fill="none" stroke="#3a4046" stroke-width="1.5"><rect x="1" y="1" width="5" height="26"/><rect x="14" y="1" width="5" height="26"/></svg>
      <svg class="overlay-icon" style="left:14px;top:132px" width="11" height="11" viewBox="0 0 11 11"><circle cx="5.5" cy="5.5" r="5.5" fill="#43b4c9"/><path d="M3 5.8l1.7 1.7L8 4" stroke="#fff" stroke-width="1.4" fill="none"/></svg>
      <svg class="overlay-icon" style="left:77px;top:131px" width="14" height="12" viewBox="0 0 14 12" fill="none" stroke="#3a4046" stroke-width="1.2"><path d="M7 11L1.5 5.8a3 3 0 0 1 5.5-3.5 3 3 0 0 1 5.5 3.5z"/></svg></div><div class="card-title">Egestas dui nec purus</div><div class="card-sub">Chris Fox</div></article>
    <article class="card"><div class="cover" role="img" aria-label="Album cover: hazy sky over hills" style="background:linear-gradient(180deg,#7d8f9c,#c5cbcc 50%,#8b8a7c 80%,#5c5a4e)"></div><div class="card-title">Aliquam sollicitudin</div><div class="card-sub">Jack Jason</div></article>
    <article class="card"><div class="cover" role="img" aria-label="Album cover: skateboarder jumping under palm trees" style="background:linear-gradient(180deg,#6f98a6,#9bb4b5 50%,#7c7260 80%,#4e4536)"></div><div class="card-title">Vestibulum ullamcorper</div><div class="card-sub">MM &amp; DD</div></article>
  </section>

  <h2 class="section-title" style="left:26px;top:504px">New Songs</h2>
  <section class="song-grid">
    <article class="song"><div class="song-art" role="img" aria-label="Black and white portrait of an artist" style="background:linear-gradient(135deg,#e8e8e8,#6a6a6a 60%,#222)"></div><div class="song-title">Spring rain</div><div class="song-sub">Miaow</div></article>
    <article class="song"><div class="song-art" role="img" aria-label="Portrait of an artist looking up" style="background:linear-gradient(135deg,#dfe6e2,#8b928c 55%,#3c4240)"></div><div class="song-title">Hope</div><div class="song-sub">Miya</div></article>
    <article class="song"><div class="song-art" role="img" aria-label="Portrait of an artist wearing headphones" style="background:linear-gradient(135deg,#7fb6c8,#c79073 55%,#7a5240)"></div><div class="song-title">Listen wind</div><div class="song-sub">Soyia Jess</div></article>
    <article class="song"><div class="song-art" role="img" aria-label="Black and white portrait of an artist" style="background:linear-gradient(135deg,#d9d9d9,#7a7a7a 55%,#2e2e2e)"></div><div class="song-title">Breaking me</div><div class="song-sub">Pett JA</div></article>
    <article class="song"><div class="song-art" role="img" aria-label="Colourful illustrated portrait" style="background:linear-gradient(135deg,#f0f0f0,#5fa0c8 45%,#e2573f)"></div></article>
    <article class="song"><div class="song-art" role="img" aria-label="Black and white portrait of an artist" style="background:linear-gradient(135deg,#f2f2f2,#9a9a9a 60%,#555)"></div></article>
    <article class="song"><div class="song-art" role="img" aria-label="Portrait of a smiling artist" style="background:linear-gradient(135deg,#3a2a22,#b57a5a 55%,#2b1d17)"></div></article>
    <article class="song"><div class="song-art" role="img" aria-label="Portrait of an artist with sunglasses" style="background:linear-gradient(135deg,#f5f5f5,#8a8a8a 55%,#1f1f1f)"></div></article>
  </section>

  <h2 class="section-title" style="left:468px;top:504px">Top Songs</h2>
  <section class="top-list">
    <div class="top-row"><span class="thumb" role="img" aria-label="Artist photo" style="background:radial-gradient(circle,#8a6a5a,#2a2220 70%)"></span><div class="meta"><div class="t">Little Town</div><div class="b">by Chris Fox</div></div><span class="rank">1</span></div>
    <div class="top-row"><span class="thumb" role="img" aria-label="Artist photo" style="background:radial-gradient(circle,#bbb,#333 70%)"></span><div class="meta"><div class="t">Lementum ligula vitae</div><div class="b">by Amanda Conlan</div></div><span class="rank">2</span></div>
    <div class="top-row"><span class="thumb" role="img" aria-label="Artist photo" style="background:radial-gradient(circle,#d8c8b0,#8a7a66 70%)"></span><div class="meta"><div class="t">Aliquam sollicitudin venenatis</div><div class="b">by Dan Doorack</div></div><span class="rank">3</span></div>
    <div class="top-row"><span class="thumb" role="img" aria-label="Artist photo" style="background:radial-gradient(circle,#9a7a6a,#3a2c26 70%)"></span><div class="meta"><div class="t">Aliquam sollicitudin venenatis</div><div class="b">by Lauren Taylor</div></div><span class="rank">4</span></div>
  </section>
</main>

<aside class="connected">
  <h2>Connected</h2>
  <div class="member" style="top:62px"><span class="pic" role="img" aria-label="Member photo" style="background:radial-gradient(circle,#e2573f,#5fa0c8 70%)"><i class="dot on"></i></span><div><div class="name">Chris Fox</div><div class="place">New York</div></div></div>
  <div class="member" style="top:132px"><span class="pic" role="img" aria-label="Member photo" style="background:radial-gradient(circle,#9a9a9a,#2a2a2a 70%)"><i class="dot on"></i></span><div><div class="name">Amanda Conlan</div><div class="place">France</div></div></div>
  <div class="member" style="top:208px"><span class="pic" role="img" aria-label="Member photo" style="background:radial-gradient(circle,#cfd2d0,#6a6e6c 70%)"><i class="dot busy"></i></span><div><div class="name">Dan Doorack</div><div class="place">Hamburg</div></div></div>
  <div class="member" style="top:281px"><span class="pic" role="img" aria-label="Member photo" style="background:radial-gradient(circle,#8a6a5a,#1f1a18 70%)"><i class="dot away"></i></span><div><div class="name">Lauren Taylor</div><div class="place">London</div></div></div>
  <div class="member" style="top:356px"><span class="pic" role="img" aria-label="Member photo" style="background:radial-gradient(circle,#eee,#444 70%)"><i class="dot on"></i></span><div><div class="name">Chris Fox</div><div class="place">Milan</div></div></div>
  <div class="member" style="top:434px"><span class="pic" role="img" aria-label="Member photo" style="background:radial-gradient(circle,#e6e6e6,#8a8a8a 70%)"><i class="dot on"></i></span><div><div class="name">Amanda Conlan</div><div class="place">Copenhagen</div></div></div>
  <div class="member" style="top:513px"><span class="pic" role="img" aria-label="Member photo" style="background:radial-gradient(circle,#c08868,#2b1d17 70%)"><i class="dot busy"></i></span><div><div class="name">Dan Doorack</div><div class="place">Barcelona</div></div></div>
  <div class="member" style="top:590px"><span class="pic" role="img" aria-label="Member photo" style="background:radial-gradient(circle,#c79073,#7fb6c8 70%)"><i class="dot on"></i></span><div><div class="name">Lauren Taylor</div><div class="place">Tokyo</div></div></div>
  <div class="member" style="top:664px"><span class="pic" role="img" aria-label="Member photo" style="background:radial-gradient(circle,#ddd,#7a7a7a 70%)"><i class="dot away"></i></span><div><div class="name">Chris Fox</div><div class="place">UK</div></div></div>
</aside>

<footer>
  <div class="me"><span class="pic" role="img" aria-label="Profile photo of John Smith"><i></i></span><div><div class="n">John.Smith ▴</div><div class="r">Art Director</div></div></div>
  <div class="player">
    <div class="controls">
      <svg width="20" height="14" viewBox="0 0 20 14" fill="none" stroke="#fff" stroke-width="1.4"><path d="M9 1L1 7l8 6zM19 1l-8 6 8 6z"/></svg>
      <svg width="20" height="26" viewBox="0 0 20 26" fill="none" stroke="#fff" stroke-width="1.4"><rect x="1" y="1" width="5" height="24"/><rect x="14" y="1" width="5" height="24"/></svg>
      <svg width="20" height="14" viewBox="0 0 20 14" fill="none" stroke="#fff" stroke-width="1.4"><path d="M1 1l8 6-8 6zM11 1l8 6-8 6z"/></svg>
      <svg width="14" height="11" viewBox="0 0 14 11" fill="none" stroke="#fff" stroke-width="1.4"><path d="M4 1.5h10M4 5.5h10M4 9.5h10M0 1.5h2M0 5.5h2M0 9.5h2"/></svg>
    </div>
    <div class="now-playing">Lentement</div>
    <div class="timeline">
      <span>02:11</span><span>03:29</span>
      <svg width="15" height="12" viewBox="0 0 15 12" fill="none" stroke="#fff" stroke-width="1.3" style="margin-left:10px"><path d="M1 4h3l4-3v10L4 8H1zM10.5 3.5a3.5 3.5 0 0 1 0 5"/></svg>
      <span class="volume"></span>
      <svg width="15" height="12" viewBox="0 0 15 12" fill="none" stroke="#fff" stroke-width="1.3" style="margin-left:12px"><path d="M0 2.5h3l6 7h5M0 9.5h3l6-7h5M12 0.5l2 2-2 2M12 7.5l2 2-2 2"/></svg>
      <svg width="15" height="13" viewBox="0 0 15 13" fill="none" stroke="#fff" stroke-width="1.3" style="margin-left:16px"><rect x="1" y="1" width="13" height="8.5" rx="1"/><path d="M5 12h5"/></svg>
    </div>
  </div>
  <div class="member-search"><svg width="12" height="12" viewBox="0 0 12 12" fill="none" stroke="#c3c8cd" stroke-width="1.5"><circle cx="5" cy="5" r="4"/><path d="M8 8l3.5 3.5"/></svg><div class="field">Search members</div></div>
</footer>

</body>
</html>
```